H-1B Visa Advertising Postcard for Immigration Law Firm

We are an employment immigration law firm in Chicago, Brannock Tisdale LLC. We are advertising to companies in the Chicago area that employ individuals on H-1B visas. New H-1B visa applications are submitted annually on April 1st. We are advertising our services and offering a 10% discount on new cases opened by January 31, 2015.
We will be using Quillpost to print the postcards. Full specifications for the oversized card is found here: http://www.quillpost-example.com/postcards.aspx?txi=48213&xnid=TopNav_Postcards_Marketing+Products&xnav=TopNav
Side 1:
- The card must include our logo, which is uploaded. Below the logo we would like our slogan, "Complete immigration solutions. Forward-Looking Advice".
- Additional text: "Let us improve your H-1B cap experience"
- Additional text: "10% off H-1B cap cases opened by January 31st". This text should be the most attention getting.
- The front side should also include space for a mailing address label and a stamp.
- Return address: Brannock Tisdale LLC, 827 W Larkmoor Ave, #518, Chicago, IL 60657
**Note to designer: If you feel that is more advantageous to place the shipping information on the reverse side, please feel free to do so.
Back side:
- Contact info: consultation@brannocktisdale.example, 312-555-0147, www.brannocktisdale.example
- Bullet points on services (below):
- Flat-fee case prices, inclusive of RFE and audit responses.
- Negotiated price locks on legal fees from 2 to 5 years.
- Innovative online case-processing platform, accessible by HR and employees from any internet connection.
- Guaranteed responses to all inquires within 24 hours.
- Quarterly reporting of visa expiration and green card processing for current employees.
**Note to designer: The contact information can go anywhere on the back side of the card.
We encourage the use of medium-weight blue as a color.
Updates
The postcard must state the words "Advertising Material" somewhere.
Target Market(s)
Computer software development companies, in particular chief executives and human resources professionals.
Industry/Entity Type
Advertising

```html
<!DOCTYPE html>
<html lang="en">
<head>
<meta charset="utf-8">
<title>Brannock Tisdale LLC – H-1B Postcard</title>
<link rel="stylesheet" href="https://fonts.googleapis.com/css2?family=Cinzel:wght@400;500&family=Tinos:ital,wght@0,400;0,700;1,400&display=swap">
<style>
  :root {
    --stage: #c8161d;
    --navy: #0b2a5c;
    --mid-blue: #1570b8;
    --light-blue: #2ea3dd;
    --bright-blue: #1fa5e8;
    --slate: #4a4f4a;
    --charcoal: #3a3b3d;
    --ink: #1b1b1b;
    --white: #ffffff;
    --photo-light: #d6d9dc;
    --photo-mid: #8c918e;
  }
  * { box-sizing: border-box; margin: 0; padding: 0; }
  html, body { width: 1200px; height: 887px; overflow: hidden; }
  body {
    background: var(--stage);
    position: relative;
    font-family: "Tinos", "Times New Roman", serif;
    color: var(--white);
  }
  .card { position: absolute; overflow: hidden; }

  /* ---------- Address side ---------- */
  .card--address {
    left: 27px; top: 28px; width: 825px; height: 530px;
    background: var(--white);
  }
  .address-band {
    position: absolute; left: 0; top: 0; width: 100%; height: 232px;
    background: var(--slate);
  }
  .address-band__photo {
    position: absolute; left: 0; top: 0; width: 300px; height: 232px;
    background: linear-gradient(90deg, var(--photo-light) 0%, var(--photo-mid) 60%, var(--slate) 100%);
  }
  .firm-name {
    position: absolute; font-family: "Cinzel", "Times New Roman", serif;
    letter-spacing: 1px; white-space: nowrap;
  }
  .address-band .firm-name { left: 212px; top: 46px; font-size: 33px; }
  .slogan { position: absolute; font-style: italic; white-space: nowrap; }
  .address-band .slogan { left: 216px; top: 94px; font-size: 17.5px; }
  .contact-list { position: absolute; list-style: none; }
  .contact-list li { display: flex; align-items: center; gap: 7px; white-space: nowrap; }
  .contact-list svg { width: 13px; height: 13px; flex: none; }
  .address-band .contact-list { left: 300px; top: 126px; font-size: 18px; line-height: 32px; }
  .address-band .contact-list li { justify-content: center; }

  .indicia {
    position: absolute; background: var(--white);
    display: flex; align-items: center; justify-content: center;
  }
  .indicia__box {
    border: 2px solid var(--ink); color: var(--ink);
    font-family: "Tinos", "Times New Roman", serif; font-weight: 700;
    text-align: center; font-size: 10.5px; line-height: 12.5px; padding: 5px 2px;
    white-space: nowrap;
  }
  .indicia__box strong { display: block; font-size: 15px; line-height: 15px; }
  .card--address .indicia { left: 697px; top: 7px; width: 120px; height: 122px; }
  .card--address .indicia__box { width: 102px; }

  /* ---------- Offer side ---------- */
  .card--offer {
    left: 364px; top: 345px; width: 802px; height: 515px;
    background: var(--white);
  }
  .offer-panel {
    position: absolute; left: 0; top: 0; width: 100%; height: 327px;
    background: linear-gradient(180deg, var(--navy) 0%, #0f4a8a 45%, var(--mid-blue) 100%);
  }
  .offer-panel .firm-name { left: 34px; top: 30px; font-size: 46px; }
  .offer-panel .slogan { left: 38px; top: 104px; font-size: 22.5px; }
  .card--offer .indicia { left: 676px; top: 6px; width: 119px; height: 118px; }
  .card--offer .indicia__box { width: 101px; }

  .headline {
    position: absolute; left: 0; width: 700px; text-align: center;
    font-family: "Cinzel", "Times New Roman", serif;
    font-size: 21px; letter-spacing: 1px; white-space: nowrap;
  }
  .headline--intro { top: 142px; }
  .headline--offer { top: 172px; }

  .services-title {
    position: absolute; left: 10px; right: 10px; top: 209px;
    display: flex; align-items: center; gap: 6px;
    font-style: italic; font-weight: 400; font-size: 21px;
  }
  .services-title::before, .services-title::after {
    content: ""; flex: 1; border-top: 1.5px dotted rgba(255,255,255,0.8);
  }
  .services {
    position: absolute; top: 242px; list-style: none;
    font-size: 13.3px; line-height: 16px;
  }
  .services li { position: relative; padding-left: 18px; margin-bottom: 5px; }
  .services li::before {
    content: ""; position: absolute; left: 0; top: 3px; width: 12px; height: 9px;
    background:
      linear-gradient(to bottom right, transparent 50%, var(--white) 50%) 0 0 / 6px 4.5px no-repeat,
      linear-gradient(to top right, transparent 50%, var(--white) 50%) 0 4.5px / 6px 4.5px no-repeat,
      linear-gradient(to bottom right, transparent 50%, var(--white) 50%) 6px 0 / 6px 4.5px no-repeat,
      linear-gradient(to top right, transparent 50%, var(--white) 50%) 6px 4.5px / 6px 4.5px no-repeat;
    transform: scaleX(-1);
  }
  .services--left { left: 22px; width: 360px; }
  .services--right { left: 408px; width: 368px; }

  .contact-panel {
    position: absolute; left: 0; top: 327px; width: 377px; height: 188px;
    background: var(--charcoal);
  }
  .contact-panel__swoosh { position: absolute; left: 0; top: 26px; width: 377px; height: 48px; }
  .contact-panel__title {
    position: absolute; left: 0; width: 300px; top: 40px; text-align: center;
    font-family: "Cinzel", "Times New Roman", serif; font-size: 18px;
    color: var(--charcoal); letter-spacing: 0.5px;
  }
  .contact-panel .contact-list {
    left: 0; width: 365px; top: 81px; font-size: 17px; line-height: 28px;
    color: var(--bright-blue);
  }
  .contact-panel .contact-list li { justify-content: center; }

  .ad-badge {
    position: absolute; left: 276px; top: 330px; width: 96px; height: 96px;
    border-radius: 50%;
    background: radial-gradient(circle at 50% 40%, #2a6fc2 0%, var(--navy) 75%);
    border: 3px solid var(--light-blue);
    display: flex; align-items: center; justify-content: center; text-align: center;
    font-style: italic; font-weight: 700; font-size: 12px; line-height: 13px;
    transform: rotate(-10deg);
  }

  .return-address {
    position: absolute; left: 410px; top: 378px; color: var(--ink);
  }
  .return-address .firm-name { position: static; font-size: 23px; }
  .return-address address {
    margin-top: 22px; font-style: normal;
    font-family: "Cinzel", "Times New Roman", serif; font-size: 17px; line-height: 29px;
  }
</style>
</head>
<body>

<!-- Address side -->
<section class="card card--address">
  <div class="address-band">
    <div class="address-band__photo" role="img" aria-label="Photo of a businessman in a grey suit ticking a checklist with a marker"></div>
    <div class="firm-name">Brannock Tisdale LLC</div>
    <p class="slogan">Complete immigration solutions. Forward-Looking Advice</p>
    <ul class="contact-list">
      <li><svg viewBox="0 0 16 16"><circle cx="8" cy="8" r="8" fill="#fff"/><path d="M5.5 4h2l.6 2-1.2.8a6 6 0 0 0 2.3 2.3l.8-1.2 2 .6v2c-3.6.3-6.8-2.9-6.5-6.5z" fill="#4a4f4a"/></svg>312-555-0147</li>
      <li><svg viewBox="0 0 16 16"><circle cx="8" cy="8" r="8" fill="#fff"/><rect x="3.5" y="5" width="9" height="6" fill="none" stroke="#4a4f4a" stroke-width="1.2"/><path d="M3.5 5l4.5 3.5L12.5 5" fill="none" stroke="#4a4f4a" stroke-width="1.2"/></svg>consultation@brannocktisdale.example</li>
      <li><svg viewBox="0 0 16 16"><circle cx="8" cy="8" r="7" fill="none" stroke="#fff" stroke-width="1.3"/><ellipse cx="8" cy="8" rx="3" ry="7" fill="none" stroke="#fff" stroke-width="1.2"/><path d="M1 8h14M2.5 4.5h11M2.5 11.5h11" stroke="#fff" stroke-width="1"/></svg>www.brannocktisdale.example</li>
    </ul>
  </div>
  <div class="indicia">
    <div class="indicia__box">Presorted<br>Standard<br>U.S. Postage<strong>PAID</strong>Permit No. 4187<br>Fontaine Valley<br>CA</div>
  </div>
</section>

<!-- Offer side -->
<section class="card card--offer">
  <div class="offer-panel">
    <div class="firm-name">Brannock Tisdale LLC</div>
    <p class="slogan">Complete immigration solutions. Forward-Looking Advice</p>
    <div class="indicia">
      <div class="indicia__box">Presorted<br>Standard<br>U.S. Postage<strong>PAID</strong>Permit No. 4187<br>Fontaine Valley<br>CA</div>
    </div>
    <p class="headline headline--intro">Let us improve your H-1B cap experience</p>
    <p class="headline headline--offer">10% off H-1B cap cases opened by January 31st</p>
    <h2 class="services-title">Our Services</h2>
    <ul class="services services--left">
      <li>Flat-fee case prices, inclusive of RFE and audit responses.</li>
      <li>Negotiated price locks on legal fees from 2 to 5 years.</li>
      <li>Quarterly reporting of visa expiration and green card processing for current employees.</li>
    </ul>
    <ul class="services services--right">
      <li>Innovative online case-processing platform, accessible by HR and employees from any internet connection.</li>
      <li>Guaranteed responses to all inquires within 24 hours.</li>
    </ul>
  </div>

  <div class="contact-panel">
    <svg class="contact-panel__swoosh" viewBox="0 0 377 48" preserveAspectRatio="none">
      <path d="M0 6 Q190 -4 377 8 L377 40 Q190 52 0 42 Z" fill="#1fa5e8"/>
      <path d="M20 10 Q160 2 300 8 L300 38 Q160 46 20 38 Z" fill="#2ab4ee"/>
    </svg>
    <p class="contact-panel__title">Contact Us:</p>
    <ul class="contact-list">
      <li><svg viewBox="0 0 16 16"><circle cx="8" cy="8" r="8" fill="#1fa5e8"/><path d="M5.5 4h2l.6 2-1.2.8a6 6 0 0 0 2.3 2.3l.8-1.2 2 .6v2c-3.6.3-6.8-2.9-6.5-6.5z" fill="#3a3b3d"/></svg>312-555-0147</li>
      <li><svg viewBox="0 0 16 16"><circle cx="8" cy="8" r="8" fill="#1fa5e8"/><rect x="3.5" y="5" width="9" height="6" fill="none" stroke="#3a3b3d" stroke-width="1.2"/><path d="M3.5 5l4.5 3.5L12.5 5" fill="none" stroke="#3a3b3d" stroke-width="1.2"/></svg>consultation@brannocktisdale.example</li>
      <li><svg viewBox="0 0 16 16"><circle cx="8" cy="8" r="7" fill="none" stroke="#1fa5e8" stroke-width="1.3"/><ellipse cx="8" cy="8" rx="3" ry="7" fill="none" stroke="#1fa5e8" stroke-width="1.2"/><path d="M1 8h14M2.5 4.5h11M2.5 11.5h11" stroke="#1fa5e8" stroke-width="1"/></svg>www.brannocktisdale.example</li>
    </ul>
  </div>

  <div class="ad-badge">Advertising<br>Material</div>

  <div class="return-address">
    <div class="firm-name">Brannock Tisdale LLC</div>
    <address>827 W Larkmoor Ave,<br>#518, Chicago, IL 60657</address>
  </div>
</section>

</body>
</html>
```